A Dedicated Thank You to my Dad

Proposed Dimensions: Approx. 20" x 30"

For Father's Day, I wrote a dedication to my Dad that encapsulates my gratitude for everything he does, and everything he is. His birthday is on August 3, but it is more important for me to transform this dedication into a meaningful and memorable gift than to meet any deadline. I would love an image that captures the relationship between a father and his son, accompanied by my words of thanks in some sort of font that is appropriate for the message (calligprahy? not sure about that).

I had actually posted the Thank You on Chatterloop as a public post, so anyone with an account can read it: https://www.chatterloop.example/photo.php?fbid=20473819265038417&set=a.918364027159.5829361.3940582&type=1&theater

Only the words starting with "Thank you ..." should be on the poster.

Target Market(s)

This is a personal gift for my Dad. He doesn't have the best of eyesight, so having the words in a really small font would not be particularly helpful. :-)

Requirements
Must have
• * Personable
* Warm
* Inviting
* Memorable
* Understated more favored over Loud
Should not have
• * An entire palette of colors
* Wacky colors or fonts

```html
<!DOCTYPE html>
<html lang="en">
<head>
<meta charset="utf-8">
<title>Thank You Dad</title>
<link href="https://fonts.googleapis.com/css2?family=Anton&family=Source+Sans+3:wght@400&display=swap" rel="stylesheet">
<style>
  :root {
    --sky-top: #2d2a2e;
    --sky-mid: #8a6a63;
    --sunset: #f0a060;
    --sun: #ffe7b0;
    --hill: #5f8a2a;
    --grass-dark: #1f2a10;
    --panel: #241a12;
    --panel-text: #f4efe8;
    --gold-light: #ffe066;
    --gold-mid: #f2b705;
    --gold-dark: #b87a00;
  }
  * { margin: 0; padding: 0; box-sizing: border-box; }
  html, body { width: 1200px; height: 800px; overflow: hidden; background: #000; }
  .poster {
    position: relative;
    width: 1200px;
    height: 800px;
    display: flex;
  }
  .scene {
    position: relative;
    width: 714px;
    height: 800px;
    background:
      radial-gradient(ellipse 260px 160px at 490px 400px, var(--sun) 0%, rgba(240,160,96,0.75) 35%, rgba(240,160,96,0) 100%),
      linear-gradient(180deg, var(--sky-top) 0%, #5a4a4e 22%, var(--sky-mid) 38%, var(--sunset) 50%, #c9a05a 56%, var(--hill) 64%, #3c5a1c 80%, var(--grass-dark) 100%);
  }
  .title {
    position: absolute;
    top: 60px;
    left: 0;
    width: 744px;
    text-align: center;
    font-family: "Anton", "Impact", sans-serif;
    font-size: 122px;
    line-height: 1.03;
    letter-spacing: 2px;
    text-transform: uppercase;
    background: linear-gradient(180deg, var(--gold-light) 0%, var(--gold-mid) 55%, var(--gold-dark) 100%);
    -webkit-background-clip: text;
    background-clip: text;
    color: transparent;
    filter: drop-shadow(0 6px 10px rgba(0,0,0,0.55));
  }
  .tribute {
    width: 486px;
    height: 800px;
    background: var(--panel);
    color: var(--panel-text);
    font-family: "Source Sans 3", "Myriad Pro", sans-serif;
    font-size: 12.1px;
    line-height: 15.85px;
    padding: 21px 14px 0 30px;
  }
  .tribute p { margin: 0; }
  .tribute .signature { margin-top: 0; }
</style>
</head>
<body>
<main class="poster">
  <section class="scene" role="img" aria-label="Sunset over green rolling hills with the silhouette of a father holding a child and two children at his sides, a station wagon parked at left and a stream in the foreground">
    <h1 class="title">Thank You<br>Dad</h1>
  </section>
  <section class="tribute">
    <p>Thank you for, after the initial shock, embracing the unexpected news that you were about to have twins.</p>
    <p>Thank you for buying enough diapers to single-handedly enable Brindle &amp; Co to make a profit.</p>
    <p>Thank you for always carrying us to the car after we fell asleep, even after we were definitely old enough to walk it.</p>
    <p>Thank you for not telling on us when we were only pretending to nap.</p>
    <p>Thank you for welcoming more people to stay with us than I can count.</p>
    <p>Thank you for sitting through more showings of "Daisy Lane" and "Comet Raiders" than any human should endure.</p>
    <p>Thank you for doggedly trying to teach me that the beach is not to be feared nor cleaned.</p>
    <p>Thank you for working two jobs, for years, to make ends meet.</p>
    <p>Thank you for loading us all up in the station wagon, pillows in tow, so we could watch the first drive-in movie together and squint in the second.</p>
    <p>Thank you for, as coach, letting me take a fake rabbit's foot onto the soccer field.</p>
    <p>Thank you for being willing to put a hit out on my guitar teacher when he beat feet.</p>
    <p>Thank you for letting me sing in my room as if I were the originating artist.</p>
    <p>Thank you for making car trips with you, wherever we were going, fun and special.</p>
    <p>Thank you for proudly and patiently taking me to my first nerd conference in junior high.</p>
    <p>Thank you for putting up with the commutes you did, for decades, so we could grow up amongst family in an incredible community.</p>
    <p>Thank you for my dry sense of humor. I cherish it.</p>
    <p>Thank you for finding a way, by hook or by crook, to send three children to college at the same time, and to allow me to go to the college of my dreams.</p>
    <p>Thank you for never giving up on trying to convince me that imperfection is not a failure.</p>
    <p>Thank you for mispronouncing, I believe on purpose, pop culture references in a way that only you can.</p>
    <p>Thank you for teaching me to try to find the good in everyone.</p>
    <p>Thank you for waiting to laugh out loud with Mom until after the police left when my camp friends and I apparently made too much noise.</p>
    <p>Thank you for showing me that there is peace to be found in stillness and quiet.</p>
    <p>Thank you for demonstrating the fun that can be had and the truths that can be gleaned from philosophical and political debate.</p>
    <p>Thank you for accepting me for who I am, no matter who I love, and for helping me to accept myself.</p>
    <p>Thank you for doing whatever you can to help whoever you can, whether friend, family or stranger.</p>
    <p>Thank you for trusting me enough to let your guard sometimes to let me know how you are truly doing.</p>
    <p>Thank you for insisting, year after year, that time with you means more than any gift I could ever purchase. That is one lesson, amongst so many, that I will pass down to our next generation.</p>
    <p class="signature">— Dee Halloran, Mark Halloran and Lisa Halloran.</p>
  </section>
</main>
</body>
</html>
```